Velumin clinic business card - double sided for young clinic

I require business cards for my aesthetic clinic specialising in the below treatments. I would like the cards to be modern as my clinic base are young 22-35 years old. I require my logo on it and would like the edges to be rounded.

I have an aesthetic clinic specialising in :
Velumin
Lip Enhancement
Chemical Peels
Facial Fillers
Non Surgical Face Lift

I would the cards to have the following information on them:
My logo - (in grey/silver)
address
Phone number
services

Colours :
White/grey/silver and red

a nice image on there, perhaps a set of lips as this is a main service i deliver

Company Name: HFA Address: 52 Harwell Lane, 4 Brimfold High Street, TN7 4QW Phone: 0207 948 2176 Website: www.helenfosburyaesthetics-example.co.uk

Target Market(s)

clinics 22-45 years old mainly female

Industry/Entity Type

Business

Contact Information for Business Card

as above

Requirements
Must have
• logo
• Address
• Email
• Phone number
• Services i offer
Nice to have
• images

```html
<!DOCTYPE html>
<html lang="en">
<head>
<meta charset="utf-8">
<title>HFA Business Card</title>
<link href="https://fonts.googleapis.com/css2?family=Libre+Baskerville:wght@400;700&family=Open+Sans:wght@400;600;700&display=swap" rel="stylesheet">
<style>
  :root {
    --backdrop: #ece9e4;
    --card: #fbfbfa;
    --ink: #3a3a3a;
    --ink-soft: #555555;
    --silver: #8e8e90;
    --silver-light: #c9c9cb;
    --red: #9c2a30;
    --skin-light: #ecd3c6;
    --skin-deep: #c99e8c;
    --edge: #d8b04a;
  }
  * { margin: 0; padding: 0; box-sizing: border-box; }
  html, body { width: 1200px; height: 800px; overflow: hidden; }
  body {
    background: var(--backdrop);
    display: flex;
    align-items: center;
    justify-content: center;
    gap: 60px;
    font-family: "Open Sans", sans-serif;
    color: var(--ink);
  }
  .card {
    position: relative;
    width: 540px;
    height: 348px;
    background: var(--card);
    border-radius: 14px;
    box-shadow: 0 0 0 2px var(--edge), 0 12px 30px rgba(0,0,0,0.12);
    overflow: hidden;
  }

  /* Back: contact side */
  .card-back { padding: 24px 30px; }
  .person-name {
    font-family: "Libre Baskerville", serif;
    font-weight: 700;
    font-size: 22px;
    letter-spacing: 0.5px;
    line-height: 1.1;
  }
  .person-role {
    font-family: "Libre Baskerville", serif;
    font-size: 16px;
    letter-spacing: 0.5px;
    margin-top: 2px;
  }
  .rule {
    border: none;
    border-top: 2px dotted var(--ink);
    width: 270px;
    margin: 10px 0;
  }
  .address, .contact-row {
    font-size: 12.5px;
    line-height: 1.45;
    color: var(--ink-soft);
  }
  .contact-list { list-style: none; margin-top: 2px; }
  .contact-row { display: flex; align-items: center; gap: 7px; }
  .contact-row svg { width: 12px; height: 12px; flex: none; fill: var(--ink); }
  .services-title {
    font-weight: 700;
    font-size: 14px;
    color: var(--ink);
  }
  .services {
    font-size: 12.5px;
    line-height: 1.5;
    color: var(--ink-soft);
  }
  .feature-image {
    position: absolute;
    right: 14px;
    bottom: 0;
    width: 210px;
    height: 220px;
  }

  /* Front: brand side */
  .card-front {
    display: flex;
    align-items: center;
    justify-content: center;
    gap: 12px;
  }
  .brand-dot {
    width: 18px;
    height: 18px;
    border-radius: 50%;
    background: var(--silver-light);
    flex: none;
  }
  .brand-name {
    font-family: "Open Sans", sans-serif;
    font-weight: 600;
    font-size: 24px;
    color: var(--silver);
  }
</style>
</head>
<body>

  <section class="card card-back">
    <h1 class="person-name">DANIEL MARSH</h1>
    <p class="person-role">CEO/FOUNDER</p>
    <hr class="rule">
    <p class="address">52 Harwell Lane<br>4 Brimfold High Street, TN7 4QW</p>
    <ul class="contact-list">
      <li class="contact-row">
        <svg viewBox="0 0 24 24" aria-hidden="true"><path d="M6.6 10.8a15.1 15.1 0 0 0 6.6 6.6l2.2-2.2a1 1 0 0 1 1-.25 11.4 11.4 0 0 0 3.6.57 1 1 0 0 1 1 1V20a1 1 0 0 1-1 1A17 17 0 0 1 3 4a1 1 0 0 1 1-1h3.5a1 1 0 0 1 1 1c0 1.25.2 2.45.57 3.6a1 1 0 0 1-.25 1z"/></svg>
        0207 948 2176
      </li>
      <li class="contact-row">
        <svg viewBox="0 0 24 24" aria-hidden="true"><path d="M2 5h20v14H2z M3 6l9 7 9-7" fill="none" stroke="#3a3a3a" stroke-width="2"/></svg>
        info@helenfosburyaesthetics-example.co.uk
      </li>
      <li class="contact-row">
        <svg viewBox="0 0 24 24" aria-hidden="true"><circle cx="12" cy="12" r="10"/></svg>
        www.helenfosburyaesthetics-example.co.uk
      </li>
    </ul>
    <hr class="rule">
    <p class="services-title">Specialising in :</p>
    <p class="services">Velumin | Lip Enhancement | Chemical Peels<br>Facial Fillers | Non Surgical Face Lift</p>

    <svg class="feature-image" viewBox="0 0 210 220" role="img" aria-label="Portrait photographs of a client framed in two overlapping red rings over soft grey shapes">
      <defs>
        <linearGradient id="skinTone" x1="0" y1="0" x2="1" y2="1">
          <stop offset="0" stop-color="#ecd3c6"/>
          <stop offset="1" stop-color="#c99e8c"/>
        </linearGradient>
      </defs>
      <rect x="10" y="30" width="190" height="170" rx="60" fill="#dcdcde"/>
      <circle cx="135" cy="62" r="54" fill="url(#skinTone)" stroke="#9c2a30" stroke-width="5"/>
      <circle cx="88" cy="160" r="56" fill="url(#skinTone)" stroke="#9c2a30" stroke-width="5"/>
    </svg>
  </section>

  <section class="card card-front">
    <span class="brand-dot" aria-hidden="true"></span>
    <p class="brand-name">Helen Fosbury Aesthetics</p>
  </section>

</body>
</html>
```